One piece Trade show banner, 8' x 8' square

One piece banner for trade show
8' x 8' airborne geophysical company

Target Market(s)

Business

Industry/Entity Type

mineral exploration and science

Colors
0054AA
0677BA
7BADD7
CADEEF
E8F1F8
FFC000
F8CF3A
FAE287
FDF2CF
FEFAEE

Requirements
Must have
• Company logo (attached), slogan (Airborne Geophysics for Discovery). We are looking for a new banner, for a standard 8 x 8' square one-piece booth. I have attached some pictures, our logo, our old banner for reference, and two examples from unrelated companies from a tradeshow that we like. If its possible I'd like to change the color of the helicopter from green to dark grey. IE, keep the orange and white, just change green to dark grey. Looking for a simple, clean design with minimal text.
Nice to have
• I have attached examples of banners that we like (2xIMG), plus our old 3-piece banner r.
Should not have
• Green in the helicopter. Please change the color of the helicopter with green/orange/white to dark grey/orange/white. IE change the green to dark grey and leave the orange and white alone. I've attached lots of pictures but I don't expect them all to be used.

```html
<!DOCTYPE html>
<html lang="en">
<head>
<meta charset="utf-8">
<title>Meridian AeroSurveys – Trade Show Banner</title>
<link rel="stylesheet" href="https://fonts.googleapis.com/css2?family=Rubik:ital,wght@0,400;0,500;0,700;1,500&family=Montserrat:wght@400&display=swap">
<style>
  :root {
    --page-bg: #e6e6e6;
    --ink-dark: #2a2a2b;
    --brand-yellow: #f9c12e;
    --paper-white: #ffffff;
    --text-light: #ffffff;
    --photo-main-top: #a9bcc4;
    --photo-main-mid: #4f7d8e;
    --photo-main-low: #2f5a60;
    --photo-rock-a: #c07b3d;
    --photo-rock-b: #6e4a2e;
    --photo-valley-a: #b9c9d3;
    --photo-valley-b: #7fa08a;
  }
  html, body {
    margin: 0;
    padding: 0;
    width: 788px;
    height: 1200px;
    overflow: hidden;
    background: var(--page-bg);
  }
  .canvas {
    position: relative;
    width: 788px;
    height: 1200px;
  }
  .banner {
    position: absolute;
    left: 24px;
    top: 230px;
    width: 740px;
    height: 740px;
    overflow: hidden;
    background: var(--ink-dark);
    font-family: "Rubik", sans-serif;
  }
  .banner-shapes {
    position: absolute;
    inset: 0;
    width: 740px;
    height: 740px;
  }
  .brand-name {
    position: absolute;
    left: 46px;
    top: 34px;
    margin: 0;
    display: flex;
    align-items: center;
    gap: 12px;
    font-family: "Rubik", sans-serif;
    font-weight: 500;
    font-size: 40px;
    line-height: 1.05;
    color: var(--ink-dark);
  }
  .brand-dot {
    width: 14px;
    height: 14px;
    border-radius: 50%;
    background: var(--brand-yellow);
    flex: none;
  }
  .slogan {
    position: absolute;
    left: 47px;
    top: 198px;
    margin: 0;
    font-weight: 500;
    font-size: 24.5px;
    line-height: 31px;
    letter-spacing: 0.4px;
    color: var(--text-light);
  }
  .service-list {
    position: absolute;
    left: 47px;
    top: 292px;
    margin: 0;
    padding: 0;
    list-style: none;
    display: grid;
    grid-template-columns: 127px auto;
    row-gap: 6px;
    font-weight: 500;
    font-size: 17px;
    line-height: 22px;
    color: var(--text-light);
  }
  .service-list li {
    display: flex;
    align-items: center;
    gap: 8px;
  }
  .service-list li::before {
    content: "";
    width: 8px;
    height: 8px;
    border-radius: 50%;
    background: var(--brand-yellow);
    flex: none;
  }
  .service-list .col-a { grid-column: 1; }
  .service-list .col-b { grid-column: 2; }
  .platforms {
    position: absolute;
    left: 50px;
    top: 416px;
    margin: 0;
    font-family: "Montserrat", sans-serif;
    font-weight: 400;
    font-size: 13px;
    color: var(--text-light);
  }
  .platforms .sep {
    font-weight: 700;
    padding: 0 2px;
  }
  .heritage {
    position: absolute;
    left: 50px;
    top: 434px;
    margin: 0;
    font-style: italic;
    font-weight: 500;
    font-size: 21px;
    line-height: 25px;
    letter-spacing: 0.3px;
    color: var(--text-light);
  }
  .web-address {
    position: absolute;
    left: 0;
    right: 0;
    top: 684px;
    margin: 0;
    text-align: center;
    font-weight: 700;
    font-size: 25px;
    line-height: 32px;
    letter-spacing: 0.3px;
    color: var(--ink-dark);
  }
</style>
</head>
<body>
<div class="canvas">
  <section class="banner" aria-label="Meridian AeroSurveys trade show banner">
    <svg class="banner-shapes" viewBox="0 0 740 740" xmlns="http://www.w3.org/2000/svg" aria-hidden="false">
      <defs>
        <linearGradient id="mainPhotoTone" x1="0" y1="0" x2="0" y2="1">
          <stop offset="0" stop-color="var(--photo-main-top)"/>
          <stop offset="0.25" stop-color="var(--photo-main-mid)"/>
          <stop offset="1" stop-color="var(--photo-main-low)"/>
        </linearGradient>
        <linearGradient id="rockPhotoTone" x1="0" y1="0" x2="1" y2="1">
          <stop offset="0" stop-color="var(--photo-rock-a)"/>
          <stop offset="1" stop-color="var(--photo-rock-b)"/>
        </linearGradient>
        <linearGradient id="valleyPhotoTone" x1="0" y1="0" x2="0" y2="1">
          <stop offset="0" stop-color="var(--photo-valley-a)"/>
          <stop offset="1" stop-color="var(--photo-valley-b)"/>
        </linearGradient>
      </defs>

      <!-- header panel -->
      <polygon class="header-panel" points="0,0 412,0 376,150 0,150" fill="var(--paper-white)"/>
      <rect class="header-rule" x="0" y="149" width="378" height="4" fill="var(--brand-yellow)"/>

      <!-- main photo area -->
      <polygon class="main-photo" role="img" aria-label="Photo: survey helicopter with sensor boom flying past a forested mountain"
               points="418,0 740,0 740,671 254,671" fill="url(#mainPhotoTone)"/>
      <!-- diagonal accent stripe -->
      <polygon class="diagonal-stripe" points="406,0 419,0 304,514 291,514" fill="var(--brand-yellow)"/>

      <!-- inset photos -->
      <polygon class="inset-frame" points="113,511 369,511 335,655 333,655 365,516 113,516" fill="var(--brand-yellow)"/>
      <polygon class="inset-photo" role="img" aria-label="Photo: survey helicopter flying between rugged orange rock cliffs"
               points="111,516 365,516 332,653 73,653" fill="url(#rockPhotoTone)"/>
      <polygon class="inset-frame" points="389,511 655,511 617,655 613,655 651,516 389,516" fill="var(--brand-yellow)"/>
      <polygon class="inset-photo" role="img" aria-label="Photo: dark grey helicopter over a green valley with distant mountains"
               points="387,516 651,516 613,653 356,653" fill="url(#valleyPhotoTone)"/>

      <!-- footer band -->
      <rect class="footer-band" x="0" y="671" width="740" height="69" fill="var(--brand-yellow)"/>
    </svg>

    <h1 class="brand-name"><span>Meridian<br>AeroSurveys</span><span class="brand-dot"></span></h1>

    <h2 class="slogan">AIRBORNE GEOPHYSICS<br>FOR DISCOVERY</h2>

    <ul class="service-list">
      <li class="col-a">TDEM</li>
      <li class="col-b">VLF-EM</li>
      <li class="col-a">Magnetics</li>
      <li class="col-b">Radiometrics</li>
      <li class="col-a">Multi-sensor</li>
    </ul>

    <p class="platforms">Helicopter<span class="sep"> I </span>Fixed Wing<span class="sep"> I </span>Drone</p>
    <p class="heritage">EXPLORING NEVADA<br>SINCE 2007</p>

    <p class="web-address">www.meridianaerosurveys.com</p>
  </section>
</div>
</body>
</html>
```